Business Card & Stationery Design for a General Contracting Company
Brenwick Contracting Limited
Tolvane Perdo
Managing Director
No 7 Marlowe Crescent, Elmsby
brenwickcontracting@quillpost.net
The Company is involved in supply and transport of aggregate materials and heavy equipment rental at present. Furthermore we recently had a project for the logo design of our Company on this website and we would like to incorporate this logo into our stationery designs and business cards. Please see the links below; Our design project; http://orders.markcraftstudio.net/contests/logo-for-a-general-contracting-company The logo chosen; http://orders.markcraftstudio.net/drafts/display/contest/512093/draft/e7d4b58213690ab1c5f93d478ee2bb718204617

```html
<!DOCTYPE html>
<html lang="en">
<head>
<meta charset="utf-8">
<title>Brenwick Contracting Limited – Business Card</title>
<link rel="stylesheet" href="https://fonts.googleapis.com/css2?family=Oswald:wght@600&family=Open+Sans:wght@400;600&display=swap">
<style>
  :root {
    --bg: #e4e5e7;
    --card: #ffffff;
    --blue: #1f5aa6;
    --blue-dark: #163f7a;
    --red: #c8202c;
    --grey: #5c5f63;
    --light-grey: #8a8d91;
  }
  * { box-sizing: border-box; margin: 0; padding: 0; }
  html, body { width: 1200px; height: 984px; overflow: hidden; }
  body {
    background: var(--bg);
    font-family: "Open Sans", sans-serif;
    display: flex;
    flex-direction: column;
    align-items: center;
    justify-content: center;
    gap: 48px;
  }
  .card {
    position: relative;
    width: 700px;
    height: 400px;
    background: var(--card);
    border-radius: 22px;
    overflow: hidden;
    box-shadow: 0 6px 18px rgba(0,0,0,0.12);
  }
  /* back */
  .card-back { display: flex; flex-direction: column; align-items: center; justify-content: center; gap: 22px; }
  .brand { display: flex; align-items: center; gap: 12px; }
  .brand-dot { width: 22px; height: 22px; border-radius: 50%; background: var(--red); flex: none; }
  .brand-name {
    font-family: "Oswald", sans-serif;
    font-weight: 600;
    text-transform: uppercase;
    color: var(--blue-dark);
    letter-spacing: 1px;
  }
  .card-back .brand-name { font-size: 34px; }
  .website { font-size: 15px; letter-spacing: 3px; color: var(--grey); }
  /* front */
  .front-art { position: absolute; inset: 0; }
  .card-front .brand { position: absolute; left: 40px; top: 44px; }
  .card-front .brand-name { font-size: 26px; }
  .holder { position: absolute; left: 40px; top: 176px; }
  .holder-name { font-size: 22px; font-weight: 600; color: var(--blue); }
  .holder-title { font-size: 15px; color: var(--grey); margin-top: 2px; }
  .contacts {
    position: absolute; left: 380px; bottom: 34px;
    list-style: none; font-size: 11px; color: var(--grey);
    display: flex; flex-direction: column; gap: 5px;
  }
  .contacts li { display: flex; align-items: center; gap: 7px; }
  .contact-icon { width: 13px; height: 13px; flex: none; }
</style>
</head>
<body>
  <section class="card card-back">
    <div class="brand">
      <span class="brand-dot"></span>
      <span class="brand-name">Brenwick Contracting Limited</span>
    </div>
    <p class="website">www.brenwickcontracting.net</p>
  </section>

  <section class="card card-front">
    <svg class="front-art" width="700" height="400" viewBox="0 0 700 400" aria-hidden="true">
      <path d="M300 0 L700 0 L700 400 L600 400 C640 250 560 70 300 0 Z" fill="var(--blue)"/>
      <path d="M0 30 C120 8 220 0 290 4 C200 6 110 20 0 48 Z" fill="var(--red)"/>
    </svg>
    <div class="brand">
      <span class="brand-dot"></span>
      <span class="brand-name">Brenwick Contracting Limited</span>
    </div>
    <div class="holder">
      <p class="holder-name">Tolvane Perdo</p>
      <p class="holder-title">Managing Director</p>
    </div>
    <ul class="contacts">
      <li><svg class="contact-icon" viewBox="0 0 16 16"><circle cx="8" cy="8" r="8" fill="var(--grey)"/><path d="M8 3.5a3 3 0 0 0-3 3c0 2.2 3 6 3 6s3-3.8 3-6a3 3 0 0 0-3-3z" fill="#fff"/></svg>No 7 Marlowe Crescent, Elmsby</li>
      <li><svg class="contact-icon" viewBox="0 0 16 16"><circle cx="8" cy="8" r="8" fill="var(--grey)"/><path d="M5 4l2 2-1 1.2a6 6 0 0 0 2.8 2.8L10 9l2 2-1.3 1.3C7.5 12 4 8.5 3.7 5.3z" fill="#fff"/></svg>868-555-0142</li>
      <li><svg class="contact-icon" viewBox="0 0 16 16"><circle cx="8" cy="8" r="8" fill="var(--grey)"/><path d="M5 4l2 2-1 1.2a6 6 0 0 0 2.8 2.8L10 9l2 2-1.3 1.3C7.5 12 4 8.5 3.7 5.3z" fill="#fff"/></svg>868-555-0178</li>
      <li><svg class="contact-icon" viewBox="0 0 16 16"><circle cx="8" cy="8" r="8" fill="var(--grey)"/><rect x="4" y="6" width="8" height="5" fill="#fff"/><rect x="5.5" y="3.5" width="5" height="2" fill="#fff"/></svg>868-555-0193</li>
      <li><svg class="contact-icon" viewBox="0 0 16 16"><circle cx="8" cy="8" r="8" fill="var(--grey)"/><rect x="3.5" y="5" width="9" height="6" fill="#fff"/><path d="M3.5 5l4.5 3.5L12.5 5" stroke="var(--grey)" fill="none"/></svg>brenwickcontracting@quillpost.net</li>
      <li><svg class="contact-icon" viewBox="0 0 16 16"><circle cx="8" cy="8" r="8" fill="var(--grey)"/><circle cx="8" cy="8" r="4.5" fill="none" stroke="#fff"/><path d="M3.5 8h9M8 3.5v9" stroke="#fff"/></svg>www.brenwickcontracting.net</li>
    </ul>
  </section>
</body>
</html>
```